ReDesign Website for a more Bold approach

Hello! I'd like to redesign my website: holvencrest.com

I'd like to add one thing that's not on my website which is a blog. The design around the blog should be put time into as I will be putting out incredibly great content and want it to attract viewers.

I get a lot of inspiration from ruvtal.com (the way they flow the big statements across each screen, colors)
moorlane.vc (the simplicity behind the design is beautiful)

I like modern very simple but bold approaches.

I am going to attach my logo here and if it can be thought of when making the design of the website. Thanks!

Industry/Entity Type

Finance and Private Equity

Number of Pages Required

3 page

Font styles to use
Serif
Sans Serif

Colors
0054AA
0677BA
7BADD7
CADEEF
E8F1F8
0094D4
00A9DD
6FCCEA
C7EBF8
E9F6FB
00AB8E
00BBA5
67D7C9
C6EFE9
E9F9F6

Requirements
Must have
• My project must have a Home, Expertise, Story, Clients, Approach, Blog, Contact
Nice to have
• It would be nice to have these tabs reduced to 1-3 pages
Should not have
• My project must not have bright colors.

```html
<!DOCTYPE html>
<html lang="en">
<head>
<meta charset="utf-8">
<title>Holvencrest Ventures — Website Design</title>
<link rel="stylesheet" href="https://fonts.googleapis.com/css2?family=Jost:wght@400;500;600&family=Playfair+Display:wght@400&display=swap">
<style>
:root{
  --navy:#0c2a44;
  --teal:#008a9a;
  --coral:#eb4746;
  --board:#e8eaed;
  --white:#ffffff;
  --ink:#2c3b4a;
  --muted:#8b96a0;
  --faint:#c9ced3;
  --serif:'Playfair Display', Georgia, serif;
  --sans:'Jost', 'Futura', Arial, sans-serif;
}
*{margin:0;padding:0;box-sizing:border-box}
html,body{width:1200px;height:3698px;overflow:hidden}
body{background:var(--board);position:relative;font-family:var(--sans);color:var(--ink)}
.abs{position:absolute}

/* style guide strip */
.guide-logo{left:234px;top:152px;font:600 19px/1 var(--sans);letter-spacing:.5px;color:var(--navy)}
.guide-divider{top:120px;width:1px;height:86px;background:var(--faint)}
.guide-label{top:122px;font:400 20px/1 var(--sans);color:var(--navy)}
.guide-serif{left:561px;top:158px;font:400 22px/1 var(--serif);color:var(--teal)}
.guide-sans{left:561px;top:187px;font:400 17px/1 var(--sans);color:var(--teal)}
.swatch{top:153px;width:38px;height:38px;border-radius:50%}
.swatch-code{top:198px;font:400 8px/1 var(--sans);color:var(--ink);width:50px;text-align:center}

/* page */
.page{left:241px;top:860px;width:717px;height:2747px;background:var(--white);overflow:hidden}
.hero{left:0;top:0;width:717px;height:458px;background:var(--navy)}
.hero-art{left:0;top:0;width:717px;height:458px;
  background:radial-gradient(ellipse 60% 45% at 45% 30%, rgba(0,138,154,.22), transparent 70%),
             radial-gradient(ellipse 70% 50% at 60% 85%, rgba(0,138,154,.25), transparent 70%)}
.nav-rule{left:0;top:53px;width:717px;height:1px;background:rgba(255,255,255,.08)}
.nav-logo{left:96px;top:21px;font:600 9px/1 var(--sans);letter-spacing:.4px;color:var(--white)}
.nav-link{top:22px;font:400 8px/1 var(--sans);color:var(--white)}
.eyebrow{left:0;width:717px;top:166px;text-align:center;font:500 9px/1 var(--sans);letter-spacing:3.5px;color:var(--coral)}
.hero-title{left:0;width:717px;top:180px;text-align:center;font:400 36px/42px var(--serif);color:var(--white)}
.hero-arrow{left:353px;top:273px}

.stat-value{top:505px;font:400 21px/1 var(--sans);color:var(--navy);letter-spacing:.5px}
.stat-value.teal{color:var(--teal)}
.stat-label{top:535px;font:400 6px/1 var(--sans);color:var(--navy);text-transform:uppercase;letter-spacing:.3px}
.stat-label.teal{color:var(--teal)}

.block-teal{background:var(--teal)}
.block-navy{background:var(--navy)}
.photo-glass{background:linear-gradient(160deg,#e9eef1 0%,#9fb2bd 45%,#2f4653 75%,#c9d5db 100%)}
.photo-team{background:linear-gradient(180deg,#d8e2e8 0%,#b7c6cf 45%,#3a4656 75%,#c7d1d7 100%)}

.section-title{font:400 27px/1 var(--serif);color:var(--navy)}
.body{font:400 7.4px/15px var(--sans);color:var(--ink)}
.body em{font-style:normal;color:var(--coral)}
.intro{left:364px;width:260px;font:400 7.4px/15px var(--sans);color:var(--ink)}

.skill{width:150px;border-left:1px solid var(--coral);padding-left:12px;height:72px}
.skill h3{font:400 10.5px/1 var(--serif);color:var(--coral);margin-top:4px;margin-bottom:16px}
.skill p{font:400 7px/14.5px var(--sans);color:var(--ink)}

.approach-text{left:364px;top:1466px;width:236px}
.approach-text p{margin-bottom:8px}

.rule-v{left:359px;top:1828px;width:1px;height:317px;background:var(--teal);opacity:.5}
.rule-h{left:96px;top:1989px;width:524px;height:1px;background:var(--teal);opacity:.5}
.article{width:230px}
.article h3{font:400 12.5px/1 var(--serif);color:var(--navy);margin-bottom:9px}
.article .meta{font:400 5.5px/1 var(--sans);color:var(--muted);margin-bottom:7px}
.article p{font:400 6.6px/14.5px var(--sans);color:var(--ink);margin-bottom:10px}
.article a{font:400 5.5px/1 var(--sans);color:var(--coral);text-decoration:underline}

.cta{left:96px;top:2200px;width:524px;height:151px;background:var(--teal);text-align:center;padding-top:47px;font:400 24px/31px var(--serif);color:var(--navy)}
.cta a{color:var(--navy);text-decoration:underline;text-decoration-thickness:1px}

.client{width:110px;text-align:center;font:500 12px/1 var(--sans);color:#d3d7da;letter-spacing:.5px}

.footer{left:0;top:2570px;width:717px;height:177px;background:var(--navy)}
.foot-head{top:52px;font:600 8px/1 var(--sans);color:var(--white);letter-spacing:.3px}
.foot-text{font:400 7px/16.5px var(--sans);color:var(--white)}
</style>
</head>
<body>

<!-- style guide -->
<div class="abs guide-logo">HOLVENCREST VENTURES</div>
<div class="abs guide-divider" style="left:501px"></div>
<div class="abs guide-label" style="left:561px">Fonts:</div>
<div class="abs guide-serif">Playfair Display</div>
<div class="abs guide-sans">Futura</div>
<div class="abs guide-divider" style="left:778px"></div>
<div class="abs guide-label" style="left:837px">Colors:</div>
<div class="abs swatch" style="left:838px;background:var(--navy)"></div>
<div class="abs swatch" style="left:885px;background:var(--teal)"></div>
<div class="abs swatch" style="left:932px;background:var(--coral)"></div>
<div class="abs swatch-code" style="left:832px">#0c2a44</div>
<div class="abs swatch-code" style="left:879px">#008a9a</div>
<div class="abs swatch-code" style="left:926px">#eb4746</div>

<main class="abs page">
  <!-- hero -->
  <section class="abs hero">
    <div class="abs hero-art" role="img" aria-label="Abstract flowing teal line pattern on navy"></div>
    <div class="abs nav-logo">HOLVENCREST VENTURES</div>
    <div class="abs nav-link" style="left:399px">Home</div>
    <div class="abs nav-link" style="left:452px">Story</div>
    <div class="abs nav-link" style="left:505px">News</div>
    <div class="abs nav-link" style="left:564px">Contact</div>
    <div class="abs nav-rule"></div>
    <div class="abs eyebrow">WELCOME TO HOLVENCREST VENTURES</div>
    <h1 class="abs hero-title">Built by Founders<br>For Founders</h1>
    <svg class="abs hero-arrow" width="10" height="18" viewBox="0 0 10 18"><path d="M5 1v15M1 12l4 4 4-4" fill="none" stroke="#eb4746" stroke-width="1"/></svg>
  </section>

  <!-- stats -->
  <div class="abs stat-value" style="left:96px">$40+</div>
  <div class="abs stat-label" style="left:96px">Money raised</div>
  <div class="abs stat-value teal" style="left:242px">$125M+</div>
  <div class="abs stat-label teal" style="left:242px">Attributed revenue</div>
  <div class="abs stat-value" style="left:418px">11</div>
  <div class="abs stat-label" style="left:418px">Company exits</div>
  <div class="abs stat-value teal" style="left:570px">2</div>
  <div class="abs stat-label teal" style="left:570px">Awards won</div>

  <!-- story -->
  <div class="abs block-teal" style="left:0;top:591px;width:89px;height:424px"></div>
  <div class="abs photo-glass" style="left:0;top:640px;width:40px;height:326px" role="img" aria-label="Glass office tower facade"></div>
  <div class="abs block-teal" style="left:422px;top:591px;width:295px;height:424px"></div>
  <div class="abs photo-glass" style="left:396px;top:640px;width:224px;height:326px" role="img" aria-label="Glass office tower seen from below"></div>
  <h2 class="abs section-title" style="left:131px;top:634px">Our Story</h2>
  <div class="abs body" style="left:131px;top:684px;width:235px">
    <p style="margin-bottom:7px">Holvencrest Ventures is a <em>venture capital studio</em> firm based in Austin TX with a laser focus on raising solid capital for startups and helping businesses jumpstart their revenue.</p>
    <p style="margin-bottom:7px"><em>Founded in 2020</em> by investment expert Daniel Marsh, Holvencrest Ventures combines proven experience in the venture capital field with a data-driven business analysis strategy to secure capital and reinforce revenue streams for startups and established businesses. Born from the idea that the best way to help founders thrive is to understand their strengths, their weaknesses, their ambitions and their needs - our specialists have been through the entire startup process themselves, and that experience forms our unique approach to business support.</p>
    <p>Daniel’s work in the sector has seen him take on the biggest and the best, working with iconic business figures to leave an indelible mark on the U.S. startup scene. He brings all of that expertise to the table at. Leading a dedicated team to support the finest international businesses to reach, break through and go beyond their potential.</p>
  </div>

  <!-- expertise -->
  <h2 class="abs section-title" style="left:96px;top:1062px">Areas of Expertise</h2>
  <p class="abs intro" style="top:1064px">Lorem ipsum dolor sit amet, consectetur adipiscing elit, sed do eiusmod  sonim tempor incididunt ut labore et dolore magna</p>
  <div class="abs skill" style="left:96px;top:1121px"><h3>Network Support</h3><p>Help you build your network,<br>introducing you to the right<br>people in the right places.</p></div>
  <div class="abs skill" style="left:297px;top:1121px"><h3>Marketing</h3><p>Consult on marketing process,<br>strategies and implementation<br>across your startup.</p></div>
  <div class="abs skill" style="left:498px;top:1121px"><h3>Raising Capital</h3><p>Reach out to our extensive<br>connections to raise vital capital<br>for your startup.</p></div>
  <div class="abs skill" style="left:96px;top:1245px"><h3>Mergers &amp; Acquisitions</h3><p>Facilitate a smooth mergers and<br>acquisition process for the<br>expansion of your business.</p></div>
  <div class="abs skill" style="left:297px;top:1245px"><h3>Revenue Acceleration</h3><p>Analyze your revenue streams,<br>providing solutions for kickstart-<br>ing your revenue.</p></div>
  <div class="abs skill" style="left:498px;top:1245px"><h3>Integration &amp; Incubation</h3><p>Providing training and guidance<br>for startups looking to make<br>their mark on the world.</p></div>

  <!-- approach -->
  <div class="abs block-navy" style="left:0;top:1368px;width:294px;height:353px"></div>
  <div class="abs photo-team" style="left:96px;top:1416px;width:226px;height:255px" role="img" aria-label="Business team in suits reviewing a tablet in a glass lobby"></div>
  <div class="abs block-navy" style="left:627px;top:1368px;width:90px;height:353px"></div>
  <div class="abs photo-team" style="left:677px;top:1416px;width:40px;height:255px" role="img" aria-label="Office interior with people"></div>
  <h2 class="abs section-title" style="left:364px;top:1415px">Our Approach</h2>
  <div class="abs body approach-text">
    <p>We’ve built our approach to helping your startup thrive based around three key developmental pillars that guarantee results for our partners.</p>
    <p><em>First pillar</em> is expertise. We’ve built our firm on a bank of insights, knowledge and proficiencies honed over years of working with the biggest names in venture capitalism – that experience forms the backbone of every project, every pitch and every investment.</p>
    <p><em>Second pillar</em> is collaboration. We believe that the best partnerships start with a combined and cooperative approach that benefits all parties every step of the way. We’ll always keep our partners up-to-date with our work using regular touchpoints and reports.</p>
    <p><em>Third and final pillar</em> is trust. We know that our clients and partners know their industry better than we do, so we trust their input and their ideas – pairing them up with our own business intelligence to success.</p>
  </div>

  <!-- articles -->
  <h2 class="abs section-title" style="left:96px;top:1768px">Latest Articles</h2>
  <p class="abs intro" style="top:1767px">Lorem ipsum dolor sit amet, consectetur adipiscing elit, sed do eiusmod  sonim tempor incididunt ut labore et dolore magna</p>
  <div class="abs rule-v"></div>
  <div class="abs rule-h"></div>
  <article class="abs article" style="left:96px;top:1858px"><h3>First article title goes here</h3><div class="meta">02.01.22 | HOLVENCREST VENTURES</div><p>Lorem ipsum dolor sit amet, consectetur adipiscing elit, sed do tom eiusmod tempor incididunt ut labore et dolore magna aliqua. Quis te ipsum suspendisse ultrices gravida.</p><a>READ MORE</a></article>
  <article class="abs article" style="left:396px;top:1858px"><h3>Second article title goes here</h3><div class="meta">02.01.22 | HOLVENCREST VENTURES</div><p>Lorem ipsum dolor sit amet, consectetur adipiscing elit, sed do tom eiusmod tempor incididunt ut labore et dolore magna aliqua. Quis te ipsum suspendisse ultrices gravida.</p><a>READ MORE</a></article>
  <article class="abs article" style="left:96px;top:2019px"><h3>Third article title goes here</h3><div class="meta">02.01.22 | HOLVENCREST VENTURES</div><p>Lorem ipsum dolor sit amet, consectetur adipiscing elit, sed do tom eiusmod tempor incididunt ut labore et dolore magna aliqua. Quis te ipsum suspendisse ultrices gravida.</p><a>READ MORE</a></article>
  <article class="abs article" style="left:396px;top:2019px"><h3>Fourth article title goes here</h3><div class="meta">02.01.22 | HOLVENCREST VENTURES</div><p>Lorem ipsum dolor sit amet, consectetur adipiscing elit, sed do tom eiusmod tempor incididunt ut labore et dolore magna aliqua. Quis te ipsum suspendisse ultrices gravida.</p><a>READ MORE</a></article>

  <!-- call to action -->
  <div class="abs cta">Got Any Project You Would Like To Discuss?<br><a>Contact Us</a></div>

  <!-- clients -->
  <h2 class="abs section-title" style="left:96px;top:2400px">Clients</h2>
  <p class="abs intro" style="top:2396px">Lorem ipsum dolor sit amet, consectetur adipiscing elit, sed do eiusmod  sonim tempor incididunt ut labore et dolore magna</p>
  <div class="abs client" style="left:87px;top:2459px">DUNMORE</div>
  <div class="abs client" style="left:206px;top:2459px">Pellway</div>
  <div class="abs client" style="left:302px;top:2459px">Sorvia</div>
  <div class="abs client" style="left:413px;top:2459px">Quenfield</div>
  <div class="abs client" style="left:531px;top:2459px">Tarnick</div>
  <div class="abs client" style="left:87px;top:2506px">VELOMARK</div>
  <div class="abs client" style="left:206px;top:2506px">Orrin Labs</div>
  <div class="abs client" style="left:302px;top:2506px">Brakefield</div>
  <div class="abs client" style="left:413px;top:2506px">Lindqvale</div>
  <div class="abs client" style="left:531px;top:2506px">Ashcombe</div>

  <!-- footer -->
  <footer class="abs footer">
    <div class="abs foot-head" style="left:96px">LINKS</div>
    <div class="abs foot-text" style="left:96px;top:70px">Home<br>Story<br>News<br>Contact</div>
    <div class="abs foot-head" style="left:270px">OFFICE</div>
    <div class="abs foot-text" style="left:270px;top:70px;line-height:13px">Street Goes Here, Avenue<br>Lorem Ipsum Dolor 94312,<br>Austin, Texas, US</div>
    <div class="abs foot-head" style="left:512px">CONTACT</div>
    <div class="abs foot-text" style="left:512px;top:70px;line-height:11px">Phone:<br>+1 234 567 890<br><br>Email:<br>daniel@holvencrest.com</div>
  </footer>
</main>

</body>
</html>
```